Business Card for Wellness Clinic

We need a business card for our new logo. I want it to match the feel of the logo

Target Market(s)

Young professional families looking for holistic health care

Industry/Entity Type

Health And Wellness

Contact Information for Business Card

Our business Name: Brackenfield Health & wellness Centre, our phone #, email address...see attached old business card

Font styles to use
Sans Serif

Colors
33b8a4
cee9f5

Requirements
Must have
• my logo and business name
• Font is "Helvetica Neue LT Std 45 Light" and
• Only for "&" using font "Trajan pro bold"
• Use colors in the logo

```html
<!DOCTYPE html>
<html lang="en">
<head>
<meta charset="utf-8">
<title>Brackenfield Health &amp; Wellness Centre – Business Card</title>
<link rel="stylesheet" href="https://fonts.googleapis.com/css2?family=Lato:wght@300;400;700&family=Cinzel:wght@400;700&display=swap">
<style>
  :root {
    --teal: #33b8a4;
    --sky: #cee9f5;
    --paper: #ffffff;
    --ink: #0a0a0a;
    --grey: #9a9a9a;
    --light-grey: #c4c4c4;
    --backdrop: #2a2a2a;
  }
  * { box-sizing: border-box; margin: 0; padding: 0; }
  html, body {
    width: 1200px; height: 900px; overflow: hidden;
    background: var(--backdrop);
    font-family: "Lato", "Helvetica Neue", Arial, sans-serif;
    font-weight: 300;
  }
  .sheet {
    width: 1200px; height: 900px;
    display: flex; flex-direction: column; align-items: center; justify-content: center;
    gap: 44px;
  }
  .card {
    width: 600px; height: 343px;
    display: flex; flex-direction: column; align-items: center;
    padding-top: 34px;
    box-shadow: 0 10px 26px rgba(0,0,0,.45);
  }
  .card--front { background: var(--paper); }
  .card--back { background: var(--ink); }

  .brand { display: flex; flex-direction: column; align-items: center; }
  .brand__mark { width: 34px; height: 34px; background: var(--teal); border-radius: 4px; margin-bottom: 8px; }
  .brand__name {
    font-family: "Lato", sans-serif; font-weight: 300;
    color: var(--grey); text-align: center; text-transform: uppercase;
    font-size: 17px; letter-spacing: 3px; line-height: 1.25;
  }

  .appointment__title { color: var(--teal); font-weight: 700; font-size: 17px; margin: 14px 0 10px; }
  .appointment__fields { width: 420px; color: var(--grey); font-size: 13px; }
  .field-row { display: flex; align-items: flex-end; gap: 6px; margin-bottom: 12px; }
  .field-line { flex: 1; border-bottom: 1px dashed var(--light-grey); height: 12px; }
  .appointment__policy {
    color: var(--teal); font-size: 13.5px; text-align: center; line-height: 1.35; margin-top: 4px;
  }
  .appointment__web { color: var(--grey); font-size: 14px; margin-top: 4px; }
  .appointment__web strong { color: var(--teal); font-weight: 700; }

  .doctor { text-align: center; margin-top: 16px; }
  .doctor__name { font-family: "Cinzel", serif; color: var(--teal); font-size: 22px; letter-spacing: .5px; }
  .doctor__title { font-family: "Cinzel", serif; color: var(--light-grey); font-size: 13px; letter-spacing: 1px; }
  .contact { text-align: center; color: var(--teal); font-size: 14px; line-height: 1.4; margin-top: 10px; }
  .contact__address { margin-bottom: 6px; }
  .contact b { font-weight: 700; }
</style>
</head>
<body>
<main class="sheet">
  <section class="card card--front">
    <div class="brand">
      <div class="brand__mark"></div>
      <div class="brand__name">Brackenfield Health<br>&amp; Wellness Centre</div>
    </div>
    <h2 class="appointment__title">Appointment</h2>
    <div class="appointment__fields">
      <div class="field-row"><span>Date:</span><span class="field-line"></span><span>Time:</span><span class="field-line"></span></div>
      <div class="field-row"><span>For:</span><span class="field-line"></span></div>
    </div>
    <p class="appointment__policy">If you are unable to keep your appointment, please provide<br>at least 2 business days notice or full visit fees will apply.</p>
    <p class="appointment__web">www.<strong>brackenfieldnaturo</strong>.ca</p>
  </section>

  <section class="card card--back">
    <div class="brand">
      <div class="brand__mark"></div>
      <div class="brand__name">Brackenfield Health<br>&amp; Wellness Centre</div>
    </div>
    <div class="doctor">
      <h1 class="doctor__name">Dr. Maren Holt, N.D.</h1>
      <p class="doctor__title">Naturopathic Doctor</p>
    </div>
    <div class="contact">
      <p class="contact__address">48 Linden Ave. E, Suite 305<br>Kingsford, ON K7L 2R8</p>
      <p><b>P:</b> 613-555-0148</p>
      <p><b>E:</b> mholt@brackenfieldnaturo.ca</p>
      <p><b>W:</b> www.brackenfieldnaturo.ca</p>
    </div>
  </section>
</main>
</body>
</html>
```